"Sun On Water" Gospel Presentation Booklet

I need a design for a 12 page (including front/back cover) square booklet, with religious images and aesthetically pleasing fonts/designs. I want it to be very simple, and very straightforward. The main focus of the project is it's content. So the design should be very nice, but also should point to the content, not take away from it, or create distraction. People should be more focused on the words than the imagery.

I enjoy modern designs, I need a sharp aesthetic that is clean and neat. Nothing over the top.
I have attached a word document with the content I would like on the pages.

Colors
0592cd
0255a3
33a6d7
85cae6
85acd3
3276b5
9bcb3b
f04a50
f68d4c

Requirements
Should not have
• Super feminine colors/aesthetics

```html
<!DOCTYPE html>
<html lang="en">
<head>
<meta charset="utf-8">
<title>Sun On Water – Booklet Spreads</title>
<link href="https://fonts.googleapis.com/css2?family=Archivo+Black&family=Bebas+Neue&display=swap" rel="stylesheet">
<style>
  :root {
    --paper: #ffffff;
    --frame: #3a3a3a;
    --rule: #cfcfcf;
    --ember: #e4603e;
    --night: #211d21;
    --ink: #0d0d0d;
  }
  html, body {
    margin: 0;
    padding: 0;
    width: 1200px;
    height: 1200px;
    overflow: hidden;
    background: var(--paper);
  }
  .sheet {
    position: relative;
    width: 1200px;
    height: 1200px;
    box-sizing: border-box;
    border: 2px solid var(--frame);
    background: var(--paper);
  }
  .page {
    position: absolute;
    width: 574px;
    height: 574px;
    box-sizing: border-box;
    border: 1px solid var(--rule);
    overflow: hidden;
  }
  .page--left { left: 25px; background: var(--paper); }
  .page--right { left: 600px; }
  .spread--man .page { top: 17px; }
  .spread--problem .page { top: 607px; }
  .page--ember { background: var(--ember); border-color: var(--ember); }
  .page--night { background: var(--night); border-color: var(--night); }

  .title-word {
    position: absolute;
    display: block;
  }
  .title-word text {
    font-family: "Archivo Black", "Arial Black", sans-serif;
  }

  .copy {
    position: absolute;
    margin: 0;
    font-family: "Bebas Neue", "Oswald", sans-serif;
    font-size: 32px;
    line-height: 35px;
    color: var(--paper);
    white-space: pre;
    z-index: 2;
  }
  .copy .gap { display: block; height: 35px; }
  .copy .line { display: block; }
  .copy .line--key-ember { color: var(--ember); }
  .copy .line--key-night { color: var(--night); }

  .highlight-band {
    position: absolute;
    background: var(--paper);
    z-index: 1;
  }
  .spread--man .highlight-band { left: 160px; top: 216px; width: 414px; height: 32px; }
  .spread--man .copy { left: 190px; top: 182px; }

  .spread--problem .highlight-band { left: 0; top: 236px; width: 414px; height: 31px; }
  .spread--problem .copy { left: 128px; top: 97px; }
</style>
</head>
<body>
<main class="sheet">

  <section class="spread spread--man">
    <div class="page page--left">
      <svg class="title-word" style="left:166px;top:240px" width="244" height="90" viewBox="0 0 244 90" role="img" aria-label="The word MAN filled with a photograph of a large crowd of people">
        <defs>
          <linearGradient id="crowdTone" x1="0" y1="0" x2="1" y2="1">
            <stop offset="0" stop-color="#8a7f78"/>
            <stop offset="0.35" stop-color="#a6574c"/>
            <stop offset="0.65" stop-color="#6f7e8c"/>
            <stop offset="1" stop-color="#9b8a6a"/>
          </linearGradient>
        </defs>
        <text x="0" y="86" font-size="104" textLength="242" lengthAdjust="spacingAndGlyphs" fill="url(#crowdTone)">MAN</text>
      </svg>
    </div>
    <div class="page page--right page--ember">
      <div class="highlight-band"></div>
      <p class="copy"><span class="line">ON THE OTHER HAND,</span><span class="line line--key-ember">MANKIND IS CORRUPT.</span><span class="gap"></span><span class="line">FOR EXAMPLE,</span><span class="line">WE ARE SELFISH,</span><span class="line">WE ARE PRIDEFUL,</span><span class="line">AND WE LIE.</span></p>
    </div>
  </section>

  <section class="spread spread--problem">
    <div class="page page--left">
      <svg class="title-word" style="left:45px;top:240px" width="500" height="90" viewBox="0 0 500 90" role="img" aria-label="The word PROBLEM with a black and white photograph of a person sitting with arms folded over their knees showing through the letters">
        <defs>
          <linearGradient id="shadowTone" x1="0" y1="0" x2="1" y2="0">
            <stop offset="0" stop-color="#0d0d0d"/>
            <stop offset="0.5" stop-color="#1a1a1a"/>
            <stop offset="0.62" stop-color="#7a7a7a"/>
            <stop offset="0.74" stop-color="#3a3a3a"/>
            <stop offset="0.85" stop-color="#151515"/>
            <stop offset="1" stop-color="#0d0d0d"/>
          </linearGradient>
        </defs>
        <text x="0" y="86" font-size="104" textLength="497" lengthAdjust="spacingAndGlyphs" fill="url(#shadowTone)">PROBLEM</text>
      </svg>
    </div>
    <div class="page page--right page--night">
      <div class="highlight-band"></div>
      <p class="copy"><span class="line">AND THERE IS OUR BIG PROBLEM:</span><span class="line">IF GOD IS PERFECT AND CORRUPTION</span><span class="line">CANNOT LIVE WITH HIM....</span><span class="line">AND WE ARE CORRUPT.....</span><span class="line line--key-night">WE CANNOT LIVE WITH GOD.</span><span class="gap"></span><span class="line">OUR CORRUPTION HAS CUT US OFF</span><span class="line">FROM GOD...NOW....</span><span class="line">AND WHEN WE DIE WHICH MEANS</span><span class="line">WE MUST SPEND ETERNITY IN A</span><span class="line">PLACE CALLED HELL...</span></p>
    </div>
  </section>

</main>
</body>
</html>
```